The Wellness Barn Business Card

Info for the front..... (in whichever order and layout looks best)
Carla Penhallow
Physiotherapist
4/37 Upper Creekbank Rd
Tallowbrook
QLD 4712
0462305178
carlapenhallow57@mailbox.example
www.thewellnessbarn.example.au
on the back I would like to be able to write appointments so probably just that heading with lines.
I like a sort of rustic style but mostly professional, colours in naturals, beige, brown, green etc. I dont mind if the logo colour is changed slightly to suit.

```html
<!DOCTYPE html>
<html lang="en">
<head>
<meta charset="utf-8">
<title>The Wellness Barn – Business Card</title>
<link rel="stylesheet" href="https://fonts.googleapis.com/css2?family=Lato:wght@300;400;700;900&family=Great+Vibes&family=Cormorant+Garamond:wght@400&display=swap">
<style>
  :root {
    --stage: #8c8c8a;
    --card: #ffffff;
    --ink: #5b544b;
    --ink-soft: #837c72;
    --rule: #6a6157;
    --line: #9a938a;
    --ghost: #eeedeb;
  }
  * { box-sizing: border-box; margin: 0; padding: 0; }
  html, body { width: 1200px; height: 907px; overflow: hidden; }
  body {
    background: var(--stage);
    font-family: "Lato", Arial, sans-serif;
    color: var(--ink);
    position: relative;
  }
  .card {
    position: absolute;
    top: 299px;
    width: 540px;
    height: 309px;
    background: var(--card);
    box-shadow: 0 6px 18px rgba(0,0,0,0.25);
    overflow: hidden;
  }
  .card--front { left: 40px; }
  .card--back { left: 620px; }

  /* Front */
  .brand {
    position: absolute;
    left: 30px;
    top: 118px;
    width: 200px;
    display: flex;
    align-items: center;
    gap: 10px;
  }
  .brand__dot {
    flex: none;
    width: 18px; height: 18px;
    border-radius: 50%;
    background: var(--ink);
  }
  .brand__name {
    font-weight: 900;
    font-size: 27px;
    line-height: 1.05;
    color: var(--ink);
  }
  .divider {
    position: absolute;
    left: 250px;
    top: 50px;
    width: 2px;
    height: 210px;
    background: var(--rule);
  }
  .contact {
    position: absolute;
    left: 275px;
    top: 48px;
    right: 20px;
  }
  .contact__name {
    font-size: 24px;
    font-weight: 400;
    color: var(--ink);
    line-height: 1.1;
  }
  .contact__role {
    font-size: 12px;
    font-weight: 300;
    color: var(--ink-soft);
    margin-bottom: 20px;
  }
  .contact__row {
    display: flex;
    align-items: flex-start;
    gap: 9px;
    font-size: 11.5px;
    color: var(--ink-soft);
    line-height: 1.4;
    margin-bottom: 5px;
  }
  .contact__row--gap { margin-top: 14px; }
  .icon { flex: none; width: 14px; height: 14px; margin-top: 1px; }

  /* Back */
  .ghost-name {
    position: absolute;
    left: 170px;
    top: 120px;
    width: 260px;
    font-weight: 900;
    font-size: 52px;
    line-height: 0.95;
    color: var(--ghost);
    text-align: center;
  }
  .heading {
    position: absolute;
    left: 28px;
    top: 22px;
  }
  .heading__pre {
    font-family: "Cormorant Garamond", Georgia, serif;
    font-size: 24px;
    color: var(--ink-soft);
    letter-spacing: 1px;
  }
  .heading__main {
    font-family: "Great Vibes", cursive;
    font-size: 58px;
    color: var(--ink);
    line-height: 0.9;
    margin-left: 10px;
  }
  .slots {
    position: absolute;
    left: 30px;
    right: 40px;
    top: 165px;
  }
  .slot {
    display: flex;
    align-items: flex-end;
    height: 34px;
  }
  .slot__label {
    width: 56px;
    font-size: 21px;
    font-weight: 400;
    color: var(--ink);
  }
  .slot__colon {
    width: 18px;
    font-size: 16px;
    color: var(--ink-soft);
  }
  .slot__line {
    flex: 1;
    border-bottom: 1px solid var(--line);
    margin-bottom: 6px;
  }
  .web {
    position: absolute;
    right: 22px;
    bottom: 14px;
    font-size: 12px;
    letter-spacing: 0.5px;
    color: var(--ink);
  }
</style>
</head>
<body>

<section class="card card--front" aria-label="Business card front">
  <div class="brand">
    <span class="brand__dot"></span>
    <span class="brand__name">The Wellness Barn</span>
  </div>
  <div class="divider"></div>
  <div class="contact">
    <h1 class="contact__name">Carla Penhallow</h1>
    <p class="contact__role">Physiotherapist</p>
    <div class="contact__row">
      <svg class="icon" viewBox="0 0 14 14"><circle cx="7" cy="7" r="6.5" fill="none" stroke="currentColor"/><path d="M7 3.2a2.4 2.4 0 0 0-2.4 2.4C4.6 7.5 7 10.6 7 10.6s2.4-3.1 2.4-5A2.4 2.4 0 0 0 7 3.2z" fill="currentColor"/></svg>
      <span>4/37 Upper Creekbank Rd<br>Tallowbrook, QLD 4712</span>
    </div>
    <div class="contact__row contact__row--gap">
      <svg class="icon" viewBox="0 0 14 14"><circle cx="7" cy="7" r="6.5" fill="none" stroke="currentColor"/><path d="M4.6 3.8l1.4-.3.8 1.8-.9.7a5 5 0 0 0 2 2l.7-.9 1.8.8-.3 1.4c-3 .3-5.8-2.5-5.5-5.5z" fill="currentColor"/></svg>
      <span>0462305178</span>
    </div>
    <div class="contact__row">
      <svg class="icon" viewBox="0 0 14 14"><circle cx="7" cy="7" r="6.5" fill="none" stroke="currentColor"/><rect x="3.6" y="4.6" width="6.8" height="4.8" fill="none" stroke="currentColor"/><path d="M3.6 4.6L7 7.3l3.4-2.7" fill="none" stroke="currentColor"/></svg>
      <span>carlapenhallow57@mailbox.example</span>
    </div>
    <div class="contact__row">
      <svg class="icon" viewBox="0 0 14 14"><circle cx="7" cy="7" r="6.5" fill="none" stroke="currentColor"/><circle cx="7" cy="7" r="3.6" fill="none" stroke="currentColor"/><path d="M3.4 7h7.2M7 3.4c-1.6 2-1.6 5.2 0 7.2M7 3.4c1.6 2 1.6 5.2 0 7.2" fill="none" stroke="currentColor" stroke-width=".8"/></svg>
      <span>www.thewellnessbarn.example.au</span>
    </div>
  </div>
</section>

<section class="card card--back" aria-label="Business card back">
  <div class="ghost-name" aria-hidden="true">The Wellness Barn</div>
  <div class="heading">
    <p class="heading__pre">Your Next</p>
    <h2 class="heading__main">Appointments</h2>
  </div>
  <div class="slots">
    <div class="slot"><span class="slot__label">Day</span><span class="slot__colon">:</span><span class="slot__line"></span></div>
    <div class="slot"><span class="slot__label">Date</span><span class="slot__colon">:</span><span class="slot__line"></span></div>
    <div class="slot"><span class="slot__label">Time</span><span class="slot__colon">:</span><span class="slot__line"></span></div>
  </div>
  <p class="web">www.thewellnessbarn.example.au</p>
</section>

</body>
</html>
```